New Business Card Design Project

Want a simple but attention grabbing business card. Back Side having mainly our logo and basic info-the front side a typical business card.

Contact Information for Business Card

Hearth & Tile Interiors
218 NW Larkspur Rd. Suite 207
Ankeny, Iowa 50021

phone- 515.482.7093

website is -htidesigns.com

```html
<!DOCTYPE html>
<html lang="en">
<head>
<meta charset="utf-8">
<title>Hearth &amp; Tile Interiors — Business Card</title>
<link href="https://fonts.googleapis.com/css2?family=Open+Sans:wght@400;700&display=swap" rel="stylesheet">
<style>
  :root {
    --backdrop: #e6e6e6;
    --brand-blue: #03a0e2;
    --brand-orange: #f15a24;
    --orange-shade: #d24d20;
    --ink-light: #ffffff;
  }
  * { margin: 0; padding: 0; box-sizing: border-box; }
  html, body {
    width: 1200px;
    height: 1144px;
    overflow: hidden;
    background: var(--backdrop);
    font-family: "Open Sans", Arial, sans-serif;
    color: var(--ink-light);
  }
  .card {
    position: absolute;
    left: 295px;
    width: 610px;
    height: 349px;
    overflow: hidden;
  }
  .card--logo-side {
    top: 194px;
    background: var(--brand-blue);
    display: flex;
    align-items: center;
    justify-content: center;
  }
  .card--contact-side {
    top: 592px;
    background: var(--brand-orange);
  }
  .brand-name {
    font-weight: 700;
    font-size: 26px;
    letter-spacing: 0.5px;
    color: var(--ink-light);
    text-align: center;
    margin-top: -6px;
  }
  .interior-photo {
    position: absolute;
    inset: 0;
    background:
      linear-gradient(90deg,
        var(--orange-shade) 0%,
        #e0531f 18%,
        var(--brand-orange) 36%,
        var(--brand-orange) 62%,
        #dc5221 80%,
        var(--orange-shade) 100%);
  }
  .contact-block {
    position: absolute;
    left: 215px;
    top: 90px;
    font-size: 18px;
    line-height: 1.2;
    white-space: nowrap;
  }
  .contact-name {
    font-weight: 400;
    margin-bottom: 17px;
  }
  .contact-name strong { font-weight: 700; }
  .contact-address { margin-bottom: 20px; }
  .contact-address .line-gap { display: block; margin-top: 2px; }
  .card-brand-mark {
    position: absolute;
    right: 27px;
    bottom: 14px;
    font-weight: 700;
    font-size: 17px;
    color: var(--ink-light);
  }
</style>
</head>
<body>
  <section class="card card--logo-side">
    <p class="brand-name">Hearth &amp; Tile Interiors</p>
  </section>

  <section class="card card--contact-side">
    <div class="interior-photo" role="img" aria-label="Orange-tinted photo of a modern bathroom with freestanding tub on the left and a kitchen with range hood and counter on the right"></div>
    <div class="contact-block">
      <p class="contact-name">EVAN <strong>MARSH</strong></p>
      <p class="contact-address">
        218 NW Larkspur Rd.
        <span class="line-gap">Suite 207</span>
        Ankeny, Iowa 50021
      </p>
      <p class="contact-phone">515.482.7093</p>
      <p class="contact-web">htidesigns.com</p>
    </div>
    <p class="card-brand-mark">Hearth &amp; Tile</p>
  </section>
</body>
</html>
```